Design The Quillbrook Hompage

See powerpoint

Industry/Entity Type

SAAS data product

Coding

Coded - Design and coding required

Number of Pages Required

4 page

Font styles to use
Sans Serif

```html
<!DOCTYPE html>
<html lang="en">
<head>
<meta charset="utf-8">
<title>Quillbrook – Public Data Made Easy</title>
<link href="https://fonts.googleapis.com/css2?family=Poppins:wght@300;400;500;600;700&display=swap" rel="stylesheet">
<style>
:root{
  --ink:#1f2638;
  --text:#3a4152;
  --muted:#5c6374;
  --blue:#6a84f2;
  --aqua:#7ecbe6;
  --grad:linear-gradient(90deg,#6a84f2,#7ecbe6);
  --footer:#1f2738;
  --soft:#f1f2f6;
  --line:#e4e6ec;
  --white:#ffffff;
}
*{margin:0;padding:0;box-sizing:border-box}
html,body{width:689px;height:1200px;overflow:hidden;background:var(--white)}
body{font-family:'Poppins',sans-serif;color:var(--ink);position:relative}
.abs{position:absolute}

/* header */
.brand{left:51px;top:26px;display:flex;align-items:center;gap:6px;font-weight:600;font-size:14px;color:var(--ink)}
.brand-dot{width:14px;height:14px;border-radius:50%;background:var(--blue)}
.nav{left:281px;top:20px;display:flex;align-items:center;font-size:7.6px;font-weight:500;letter-spacing:.2px}
.nav a{color:var(--ink);text-decoration:none;margin-right:19px}
.btn{display:inline-flex;align-items:center;justify-content:center;border-radius:13px;font-weight:600;font-size:7.6px;text-decoration:none}
.btn-grad{background:var(--grad);color:var(--white)}
.btn-line{border:1.2px solid var(--ink);color:var(--ink);background:var(--white)}
.signup{left:503px;top:14px;width:65px;height:26px}
.login{left:573px;top:14px;width:65px;height:26px}
.header-rule{left:213px;top:55px;width:476px;height:1px;background:var(--line)}

/* hero */
.hero-title{left:50px;top:111px;font-size:38px;line-height:41px;font-weight:700;letter-spacing:-.3px}
.grad-text{background:var(--grad);-webkit-background-clip:text;background-clip:text;color:transparent}
.hero-copy{left:51px;width:250px;font-size:8px;line-height:12.7px;font-weight:300;color:var(--text)}
.cta-register{left:53px;top:296px;width:151px;height:25px;font-size:7.6px}
.cta-pricing{left:211px;top:296px;width:64px;height:25px}
.hero-art{left:321px;top:78px;width:368px;height:349px}

/* developers */
.section-title{left:0;top:414px;width:689px;text-align:center;font-size:20.5px;line-height:28px;font-weight:600}
.section-copy{left:144px;top:480px;width:401px;text-align:center;font-size:8px;line-height:12.7px;font-weight:300;color:var(--text)}
.feature{width:180px;text-align:center}
.feature-disc{width:83px;height:83px;border-radius:50%;background:radial-gradient(circle at 50% 30%,#f6f7fa,#eef0f4);margin:0 auto;position:relative}
.feature-disc svg{position:absolute;left:21px;top:34px}
.feature h3{font-size:11.5px;font-weight:600;margin-top:16px;line-height:14px}
.feature p{font-size:7.9px;line-height:12.7px;font-weight:300;color:var(--text);margin-top:3px}

/* footer */
.footer-wave{left:0;top:896px;width:689px;height:70px}
.footer{left:0;top:950px;width:689px;height:250px;background:var(--footer);color:var(--white)}
.footer-brand{left:69px;top:1030px;display:flex;align-items:center;gap:7px;font-size:15px;font-weight:600}
.footer-brand .brand-dot{width:16px;height:16px}
.footer-about{left:69px;top:1075px;width:160px;font-size:7.8px;line-height:12.7px;font-weight:300;color:#e6e9f0}
.foot-col h4{font-size:11px;font-weight:600;margin-bottom:13px}
.foot-col a{display:block;color:#dfe3ea;text-decoration:none;font-size:7.5px;font-weight:300;line-height:15.3px}
.contact-line{display:flex;gap:5px;font-size:7.5px;font-weight:300;line-height:11px;color:#dfe3ea}
.socials{display:flex;gap:4px;margin-top:15px}
.socials span{width:22px;height:22px;border-radius:50%;background:#2d3548}
.foot-rule{left:51px;top:1159px;width:587px;height:1px;background:#3a4255}
.copyright{left:0;top:1171px;width:689px;text-align:center;font-size:7.6px;color:#e6e9f0}
.to-top{left:653px;top:1148px;width:23px;height:23px;border-radius:50%;background:var(--grad);display:flex;align-items:center;justify-content:center}
</style>
</head>
<body>

<header>
  <div class="abs brand"><span class="brand-dot"></span>Quillbrook</div>
  <nav class="abs nav">
    <a href="#">PRICING</a><a href="#">DOCUMENTATION</a><a href="#">DATA</a><a href="#">BLOG</a>
  </nav>
  <a href="#" class="abs btn btn-grad signup">SIGNUP</a>
  <a href="#" class="abs btn btn-line login">LOGIN</a>
  <div class="abs header-rule"></div>
</header>

<section class="hero">
  <h1 class="abs hero-title">Public <span class="grad-text">Data</span><br>Made Easy</h1>
  <p class="abs hero-copy" style="top:210px">From demographics to economics, from weather to health, on country level or community level. The Quillbrook collects many public data sources and organizes it for you.</p>
  <p class="abs hero-copy" style="top:258px">Use The Quillbrook API or SDK to easily get public data from many different sources.</p>
  <a href="#" class="abs btn btn-grad cta-register">REGISTER AND START FOR FREE</a>
  <a href="#" class="abs btn btn-line cta-pricing">PRICING</a>
  <svg class="abs hero-art" viewBox="0 0 368 349" role="img" aria-label="Illustration of two analysts working with dashboards, charts and a desk computer">
    <defs><linearGradient id="artBg" x1="0" y1="0" x2="1" y2="1"><stop offset="0" stop-color="#f4f5f8"/><stop offset="1" stop-color="#eceef3"/></linearGradient></defs>
    <path d="M60 120C60 60 120 20 200 10C280 0 368 40 368 70L368 349C320 345 290 320 250 315C190 308 160 300 120 280C70 255 0 240 10 180C18 140 60 150 60 120Z" fill="url(#artBg)"/>
    <rect x="42" y="22" width="228" height="84" rx="9" fill="#e3e8f7"/>
    <rect x="70" y="112" width="70" height="108" rx="7" fill="#e3e8f7"/>
    <rect x="146" y="112" width="142" height="130" rx="7" fill="#e3e8f7"/>
  </svg>
</section>

<section class="developers">
  <h2 class="abs section-title">Designed for <span class="grad-text">Developers</span><br>In Need of Data</h2>
  <p class="abs section-copy">As a data scientist or engineer you always are looking for getting more data in with more efficiency. This is exactly what The Quillbrook is making possible for you.</p>

  <div class="abs feature" style="left:48px;top:521px">
    <div class="feature-disc"><svg width="41" height="41" viewBox="0 0 41 41" fill="none" stroke="#1f2638" stroke-width="1.3"><rect x="1" y="4" width="34" height="30" rx="2"/><line x1="1" y1="10" x2="35" y2="10"/><text x="5" y="20" font-size="8" font-family="Poppins,sans-serif" font-weight="600" fill="#1f2638" stroke="none">API</text><line x1="5" y1="25" x2="18" y2="25"/><line x1="5" y1="29" x2="15" y2="29"/><circle cx="31" cy="30" r="6" stroke="#6a84f2" fill="#fff"/><circle cx="31" cy="30" r="2.5" stroke="#6a84f2"/></svg></div>
    <h3>Many Sources</h3>
    <p>Public data comes from many sources, all with their own data format &amp; interface. No longer worry about these differences, The Quillbrook collects &amp; standardizes it for you.</p>
  </div>
  <div class="abs feature" style="left:254px;top:521px">
    <div class="feature-disc"><svg width="41" height="41" viewBox="0 0 41 41" fill="none" stroke="#1f2638" stroke-width="1.3"><rect x="4" y="12" width="34" height="22" rx="2"/><line x1="16" y1="38" x2="26" y2="38"/><line x1="21" y1="34" x2="21" y2="38"/><circle cx="21" cy="20" r="5" stroke="#6a84f2"/><circle cx="21" cy="20" r="2" stroke="#6a84f2"/><circle cx="8" cy="6" r="2"/><circle cx="34" cy="6" r="2"/><circle cx="21" cy="3" r="2"/></svg></div>
    <h3>Integrate</h3>
    <p>Use the Quillbrook API to combine Public data with your own comapny data and create value for your business.</p>
  </div>
  <div class="abs feature" style="left:463px;top:521px">
    <div class="feature-disc"><svg width="41" height="41" viewBox="0 0 41 41" fill="none" stroke="#1f2638" stroke-width="1.3"><circle cx="18" cy="22" r="16"/><path d="M6 16c6 2 8 8 5 12M22 8c-2 5 4 8 8 6M18 38c1-6 6-8 10-5"/><path d="M34 2a5 5 0 0 1 5 5c0 4-5 9-5 9s-5-5-5-9a5 5 0 0 1 5-5z" stroke="#6a84f2"/><circle cx="34" cy="7" r="1.8" stroke="#6a84f2"/></svg></div>
    <h3>Regional</h3>
    <p>Do you need regional information in your pipeline ? The Quillbrook provides public data up to community level.</p>
  </div>

  <div class="abs feature" style="left:48px;top:712px">
    <div class="feature-disc"><svg width="41" height="41" viewBox="0 0 41 41" fill="none" stroke="#1f2638" stroke-width="1.3"><rect x="9" y="9" width="23" height="23" rx="2"/><circle cx="20.5" cy="20.5" r="5" stroke="#6a84f2"/><circle cx="20.5" cy="20.5" r="2" stroke="#6a84f2"/><path d="M14 9V3M20.5 9V2M27 9V3M14 32v6M20.5 32v7M27 32v6M9 14H3M9 20.5H2M9 27H3M32 14h6M32 20.5h7M32 27h6"/></svg></div>
    <h3>Automate</h3>
    <p>Use the latest public data in your data pipeline as the Quillbrook makes daily updates to the data. You no longer need to worry about multiple differnt data sources.</p>
  </div>
  <div class="abs feature" style="left:254px;top:712px">
    <div class="feature-disc"><svg width="41" height="41" viewBox="0 0 41 41" fill="none" stroke="#1f2638" stroke-width="1.3"><rect x="9" y="1" width="23" height="13" rx="2" stroke="#6a84f2"/><text x="12" y="11" font-size="9" font-family="Poppins,sans-serif" fill="#6a84f2" stroke="none">SDK</text><path d="M3 22l17-8 18 8-18 8z"/><path d="M6 24v10l14 6 14-6V24M20 30v10"/></svg></div>
    <h3>The Quillbrook SDK</h3>
    <p>Use our SDK to access our data without any knowledge of our API.</p>
  </div>
  <div class="abs feature" style="left:463px;top:712px">
    <div class="feature-disc"><svg width="41" height="41" viewBox="0 0 41 41" fill="none" stroke="#1f2638" stroke-width="1.3"><rect x="3" y="6" width="26" height="22" rx="2"/><rect x="9" y="1" width="16" height="10" rx="1"/><line x1="12" y1="5" x2="22" y2="5"/><circle cx="19" cy="25" r="7" stroke="#6a84f2"/><line x1="24" y1="30" x2="34" y2="40" stroke="#6a84f2"/></svg></div>
    <h3>Tracable</h3>
    <p>For all data we give you the legends as well as the sources from which we retrieve the data. So you always know what the data is exactly about.</p>
  </div>
</section>

<footer>
  <svg class="abs footer-wave" viewBox="0 0 689 70" preserveAspectRatio="none">
    <defs><linearGradient id="waveGrad" x1="0" x2="1"><stop offset="0" stop-color="#6a84f2"/><stop offset="1" stop-color="#7ecbe6"/></linearGradient></defs>
    <path d="M0 4C60 30 120 40 220 48C330 56 420 40 520 22C600 8 650 6 689 8V70H0Z" fill="url(#waveGrad)"/>
    <path d="M0 26C80 44 150 52 240 55C340 58 440 40 540 28C610 20 660 22 689 28V70H0Z" fill="#1f2738"/>
  </svg>
  <div class="abs footer" style="top:960px;height:240px"></div>
  <div class="abs footer-brand"><span class="brand-dot"></span>Quillbrook</div>
  <p class="abs footer-about">The Quillbrook was created to simplify access to public data and save you countless hours of manual collection</p>

  <div class="abs foot-col" style="left:250px;top:998px;color:#fff">
    <h4>Our Product</h4>
    <a href="#">Introduction</a><a href="#">The datamodels</a><a href="#">The API</a><a href="#">The SDK</a>
  </div>
  <div class="abs foot-col" style="left:368px;top:998px;color:#fff">
    <h4>The Company</h4>
    <a href="#">About</a><a href="#">Frequently Asked Questions</a><a href="#">Privacy Policy</a><a href="#">Cookie Policy</a><a href="#">Terms of Service</a>
  </div>
  <div class="abs foot-col" style="left:512px;top:998px;color:#fff">
    <h4>Contact Us</h4>
    <div class="contact-line">
      <svg width="11" height="9" viewBox="0 0 11 9"><rect width="11" height="9" rx="1" fill="#6a84f2"/><path d="M0.5 1l5 4 5-4" fill="none" stroke="#1f2738" stroke-width="1"/></svg>
      <span>Email:<br>hello@quillbrook-data.io</span>
    </div>
    <div class="socials"><span></span><span></span></div>
  </div>

  <div class="abs foot-rule"></div>
  <p class="abs copyright">© 2024 The Quillbrook. All rights reserved.</p>
  <div class="abs to-top"><svg width="7" height="5" viewBox="0 0 7 5"><path d="M1 4l2.5-2.5L6 4" fill="none" stroke="#fff" stroke-width="1.2"/></svg></div>
</footer>

</body>
</html>
```